WTF!!! We need a modern professional website for a business litigation law firm.

We need a modern, clean, professional and uncomplicated website for a new business trial and litigation law firm called "Hallorand Trial Firm PLLC". Website must be mobile optimized for iPad and smartphone. The law firm specializes in counseling and representing large corporations, small businesses and entrepreneurs in and out of the courtroom. Lawyers in the firm serve as Florida counsel and trial counsel to organizations facing claims involving product liability, premises liability, professional liability, vehicle and transportation liability, warranty claims, construction defects and delay claims, complex business disputes, commercial litigation and bid disputes in State and Federal Courts. The website is mainly to provide information about the firm, and should include sections describing the firm, identifying the Industries Served and Areas of Practice ," a separate page identifying the "Professionals", a separate page for "Resources & Advisories," and a traveling "Connect With Us" button a site visitor can click on that will launch an email to the Firm's general email account. The website should allow us to easily modify the content on these pages, and let us add/modify links to external information sources. We will not sell anything or take payments through the website. We do need to be able to easily upload and update photographs of attorneys and add new attorneys names/email hyperlinks as the firm grows. We would like to add developments in the law or success stories easily and quickly, such as through a blog page. On the "Connect With Us" page the website should have hyperlinks to email the Firm, and there should be hyperlinks to email each professional on the "Professionals" page. The website should be viewable on mobile devices without distortion. The law firm focuses on trial work and should have some imagery associated with courtrooms, but the overall theme of the site should be modern, clean, and communicate sophistication and strength. The website should be made in Wordpress. We have uploaded logo files for Hallorand Trial Firm.

Target Market(s)

Corporations and companies that are looking for legal representation. Other attorneys/legal industry.

Industry/Entity Type

Legal Industry

Coding

Coded - Design and coding required

Number of Pages Required

1 page

Font styles to use
Sans Serif

Requirements
Must have
• Simple, clean, sophisticated, modern website that includes the logo, watermark of logo, and the elements described above.
Nice to have
• Pictures of city scape, buildings, courtroom, team members.

```html
<!DOCTYPE html>
<html lang="en">
<head>
<meta charset="utf-8">
<title>Hallorand Trial Firm</title>
<link href="https://fonts.googleapis.com/css2?family=Poppins:ital,wght@0,300;0,400;0,500;0,600;0,700;1,300&display=swap" rel="stylesheet">
<style>
:root{
  --orange:#cd8546;
  --ink:#2a2a35;
  --muted:#8b8b95;
  --paper:#f3f2ef;
  --white:#ffffff;
  --teal:#1d5254;
  --band:#2c2b2e;
  --navy:#2e2b42;
  --field:#f5f5f5;
}
*{box-sizing:border-box;margin:0;padding:0}
html,body{width:1200px;height:4246px;overflow:hidden}
body{font-family:'Poppins',sans-serif;background:var(--paper);color:var(--ink);position:relative}
.abs{position:absolute}
.ph{position:absolute;display:block}

/* partners */
.partners-hero{left:0;top:0;width:1200px;height:540px;background:linear-gradient(90deg,#3a2e26,#5b4a3c 30%,#4a3a2f 60%,#2f2620)}
.partners-title{left:0;width:1200px;top:68px;text-align:center;color:var(--white);font-size:29px;font-weight:600}
.view-people{left:0;width:1200px;top:130px;text-align:center;color:var(--orange);font-size:13px;font-weight:500;letter-spacing:.5px}
.partner-card{top:250px;width:350px;height:388px;background:var(--white);text-align:center}
.partner-card .ph{left:0;top:0;width:350px;height:290px}
.partner-name{position:absolute;left:0;right:0;top:318px;font-size:16px;font-weight:500;letter-spacing:1px}
.partner-role{position:absolute;left:0;right:0;top:346px;font-size:12px;color:var(--muted);letter-spacing:1.5px}
.nav-btn{top:672px;width:56px;height:55px;background:var(--white);display:flex;align-items:center;justify-content:center}

/* testimonials */
.section-title{left:0;width:1200px;top:876px;text-align:center;font-size:38px;font-weight:400}
.video-card{left:94px;top:1013px;width:470px;height:437px;background:var(--teal)}
.video-card .ph{left:0;top:0;width:470px;height:266px;background:linear-gradient(120deg,#4a4a4a,#8a8a8a 50%,#3a3a3a)}
.play{left:191px;top:88px;width:90px;height:90px;border-radius:50%;background:rgba(255,255,255,.85)}
.video-title{left:28px;top:290px;color:var(--white);font-size:25px;line-height:27px;font-weight:400;width:400px}
.video-text{left:28px;top:362px;color:var(--white);font-size:13.5px;line-height:21px;width:400px}
.avatar{width:80px;height:80px;border-radius:50%;border:3px solid var(--white);background:linear-gradient(135deg,#555,#222)}
.client-name{font-size:14px;font-weight:600;width:110px;text-align:center}
.quote{left:697px;width:391px;height:132px;background:var(--white);font-size:13.5px;font-style:italic;font-weight:300;color:#666;line-height:21px;padding:16px 30px;text-align:center}
.dot{top:1467px;width:13px;height:13px;border-radius:50%;background:#c8cfcf}

/* consultation */
.consult{left:240px;top:1689px;width:719px;height:615px;background:var(--white);box-shadow:0 6px 26px rgba(0,0,0,.18)}
.consult-title{left:0;width:719px;top:60px;text-align:center;font-size:28px;font-weight:700}
.consult-sub{left:110px;width:500px;top:112px;text-align:center;font-size:15px;line-height:26px;color:#8a7a6a}
.field{background:var(--field);font-size:14px;color:#999;padding:0 18px;display:flex;align-items:center}
.submit{left:65px;top:504px;width:590px;height:55px;background:var(--orange);color:var(--white);font-size:13px;font-weight:500;display:flex;align-items:center;justify-content:center;border-radius:3px}

/* help band */
.help{left:0;top:2413px;width:1200px;height:511px;background:linear-gradient(90deg,#2a2927,#3a3733 50%,#2a2927)}
.help-kicker{left:0;width:1200px;top:56px;text-align:center;color:var(--white);font-size:20px;font-weight:500}
.help-call{left:0;width:1200px;top:93px;text-align:center;color:var(--orange);font-size:27px;font-weight:400}
.help-info{left:0;width:1200px;top:160px;display:flex;justify-content:center;gap:28px;color:var(--white);font-size:13.5px;font-weight:600}
.help-info span{display:flex;align-items:center;gap:10px}
.help-rule{left:599px;top:212px;width:1px;height:27px;background:#888}
.news-title{left:0;width:1170px;top:280px;text-align:center;color:var(--white);font-size:33px;font-weight:600}
.news-input{left:356px;top:352px;width:321px;height:55px;background:#4a4846;color:#bbb;font-size:13.5px;padding:0 18px;display:flex;align-items:center}
.news-btn{left:677px;top:352px;width:149px;height:55px;background:var(--orange);color:var(--white);font-size:14.5px;display:flex;align-items:center;justify-content:center}

/* blog */
.blog{left:0;top:2924px;width:1200px;height:812px;background:var(--white)}
.kicker{left:33px;top:62px;color:var(--orange);font-size:21px;font-weight:500;letter-spacing:1px}
.blog-title{left:33px;top:106px;font-size:46px;font-weight:700;color:#33313f}
.all-posts{left:974px;top:116px;width:183px;height:52px;background:var(--orange);color:var(--white);font-size:13px;font-weight:500;display:flex;align-items:center;justify-content:center}
.post{top:276px;width:356px;height:444px;background:var(--white);box-shadow:0 2px 12px rgba(0,0,0,.1)}
.post .ph{left:0;top:0;width:356px;height:234px}
.post-title{position:absolute;left:28px;top:270px;width:300px;font-size:23px;line-height:28px;font-weight:700;color:#3a3846}
.post-meta{position:absolute;left:0;right:0;top:394px;border-top:1px solid #eee;padding:18px 28px;font-size:15px;color:#aaa}

/* footer */
.footer{left:0;top:3736px;width:1200px;height:510px;background:var(--navy)}
.brand{left:56px;top:112px;display:flex;align-items:center;gap:10px;color:var(--white);font-size:22px;font-weight:700}
.brand i{display:block;width:14px;height:14px;background:var(--white)}
.footer-about{left:56px;top:205px;width:270px;color:#a9a7b8;font-size:13.5px;line-height:21px}
.social{top:337px;width:38px;height:38px;border-radius:50%;background:var(--orange)}
.col-title{top:118px;color:var(--white);font-size:21px}
.col-text{color:#d9d8e4;font-size:12.5px;line-height:25px}
.col-list{color:#d9d8e4;font-size:11px;font-weight:600;line-height:33px;letter-spacing:.3px}
.bottom{left:0;top:462px;width:1200px;display:flex;justify-content:space-between;padding:0 40px 0 46px;font-size:14px;color:#a9a7b8}
.bottom nav{display:flex;gap:28px;color:#d9d8e4}
.bottom nav b{color:var(--white);font-weight:600}
</style>
</head>
<body>

<!-- Partners -->
<div class="abs partners-hero ph" role="img" aria-label="Library with shelves of law books and marble busts"></div>
<h2 class="abs partners-title">Partners at Hallorand</h2>
<div class="abs view-people">VIEW ALL PEOPLE →</div>

<div class="abs partner-card" style="left:38px">
  <div class="ph" role="img" aria-label="Portrait of partner in a dark suit" style="background:linear-gradient(180deg,#e8e8e8,#9a9a9a 60%,#222)"></div>
  <div class="partner-name">CONRAD ASHBY</div><div class="partner-role">PARTNER</div>
</div>
<div class="abs partner-card" style="left:425px">
  <div class="ph" role="img" aria-label="Portrait of partner in a navy blouse" style="background:linear-gradient(180deg,#8a92a8,#6c7286 55%,#3b3f56)"></div>
  <div class="partner-name">LAURA PENNICK</div><div class="partner-role">PARTNER</div>
</div>
<div class="abs partner-card" style="left:812px">
  <div class="ph" role="img" aria-label="Portrait of partner in a blue jacket" style="background:linear-gradient(180deg,#e2e2e4,#c8c8cc 50%,#2d4b8c)"></div>
  <div class="partner-name">SOFIA MARLOWE</div><div class="partner-role">PARTNER</div>
</div>
<div class="abs nav-btn" style="left:534px"><svg width="14" height="22" viewBox="0 0 14 22"><path d="M11 2 3 11l8 9" fill="none" stroke="#cd8546" stroke-width="1.5"/></svg></div>
<div class="abs nav-btn" style="left:610px"><svg width="14" height="22" viewBox="0 0 14 22"><path d="M3 2l8 9-8 9" fill="none" stroke="#cd8546" stroke-width="1.5"/></svg></div>

<!-- Testimonials -->
<h2 class="abs section-title">What Our Clients Say</h2>
<div class="abs video-card">
  <div class="ph" role="img" aria-label="Black and white interview scene in an office"></div>
  <div class="abs play"></div>
  <svg class="abs" style="left:226px;top:115px" width="30" height="36" viewBox="0 0 30 36"><path d="M2 2l26 16L2 34z" fill="#222"/></svg>
  <div class="abs video-title">An Interview With Gerald Whitcombe</div>
  <div class="abs video-text">comparison between various cival law and private law institutions cases.</div>
</div>

<div class="abs avatar" style="left:596px;top:989px" role="img" aria-label="Client portrait"></div>
<div class="abs client-name" style="left:580px;top:1078px">Owen Hale</div>
<div class="abs quote" style="top:967px">Hallorand Trial Firm provided exceptional legal guidance and achieved the results we needed</div>

<div class="abs avatar" style="left:598px;top:1159px;background:linear-gradient(135deg,#7a4a2a,#2a1a10)" role="img" aria-label="Client portrait"></div>
<div class="abs client-name" style="left:583px;top:1248px">Nadia Ross</div>
<div class="abs quote" style="top:1137px">Their expertise and dedication made all the difference in our case.</div>

<div class="abs avatar" style="left:598px;top:1328px;background:linear-gradient(135deg,#bbb,#444)" role="img" aria-label="Client portrait"></div>
<div class="abs client-name" style="left:583px;top:1418px">Victor Dunn</div>
<div class="abs quote" style="top:1307px">Top-tier representation with a results-driven approach—we highly recommend them</div>

<div class="abs dot" style="left:1031px;background:var(--teal)"></div>
<div class="abs dot" style="left:1055px"></div>
<div class="abs dot" style="left:1078px"></div>

<!-- Consultation -->
<div class="abs consult">
  <div class="ph" role="img" aria-label="Faint statue of Lady Justice" style="left:430px;top:100px;width:200px;height:480px;background:radial-gradient(ellipse at center,rgba(0,0,0,.05),rgba(0,0,0,0) 70%)"></div>
  <h3 class="abs consult-title">Free Consultation</h3>
  <p class="abs consult-sub">Law is complicate matter. it can cause you a big problem &nbsp;if you ignore it. Let us help you!</p>
  <div class="abs field" style="left:65px;top:211px;width:288px;height:55px">Name*</div>
  <div class="abs field" style="left:366px;top:211px;width:289px;height:55px">Phone*</div>
  <div class="abs field" style="left:65px;top:289px;width:288px;height:52px;color:#444;justify-content:space-between">Product Liability<svg width="11" height="7" viewBox="0 0 11 7"><path d="M0 0h11L5.5 7z" fill="#333"/></svg></div>
  <div class="abs field" style="left:366px;top:289px;width:289px;height:52px">Email*</div>
  <div class="abs field" style="left:65px;top:363px;width:590px;height:120px;align-items:flex-start;padding-top:14px">Message*</div>
  <div class="abs submit">SUBMIT NOW</div>
</div>

<!-- Help band -->
<div class="abs help">
  <div class="ph" role="img" aria-label="Dim photo of a lawyer's desk with gavel" style="left:0;top:0;width:1200px;height:511px;background:radial-gradient(ellipse at 50% 40%,rgba(90,80,70,.35),rgba(0,0,0,0) 70%)"></div>
  <div class="abs help-kicker">ARE YOU LOOKING FOR SOMEONE TO HELP?</div>
  <div class="abs help-call">Let Us Help You! Call Now : (5)5501-2468-90</div>
  <div class="abs help-info">
    <span><svg width="20" height="16" viewBox="0 0 20 16"><rect x="1" y="3" width="18" height="12" fill="none" stroke="#cd8546" stroke-width="1.4"/><path d="M1 3l9 7 9-7" fill="none" stroke="#cd8546" stroke-width="1.4"/></svg>Contact @Hallorand .com</span>
    <span><svg width="18" height="18" viewBox="0 0 18 18"><circle cx="9" cy="9" r="7.5" fill="none" stroke="#cd8546" stroke-width="1.4"/><path d="M9 4v5l3 2" fill="none" stroke="#cd8546" stroke-width="1.4"/></svg>Mon–Fri 9:00–17:00</span>
  </div>
  <div class="abs help-rule"></div>
  <h3 class="abs news-title">Subscribe To Newsletter</h3>
  <div class="abs news-input">Your Email Address</div>
  <div class="abs news-btn">Subscribe</div>
</div>

<!-- Blog -->
<div class="abs blog">
  <div class="abs kicker">OUR BLOG</div>
  <h2 class="abs blog-title">Latest News &amp; Updates</h2>
  <div class="abs all-posts">VIEW ALL POSTS</div>
  <div class="abs" style="left:42px;top:200px;width:26px;height:3px;background:var(--orange)"></div>
  <div class="abs" style="left:80px;top:200px;width:90px;height:3px;background:var(--navy)"></div>

  <div class="abs post" style="left:38px">
    <div class="ph" role="img" aria-label="Wooden gavel with coins" style="background:radial-gradient(circle at 40% 50%,#9a5a30,#2a1a12 70%)"></div>
    <div class="post-title">What To Do If Teammates Do Not Appreciate You?</div>
    <div class="post-meta">Admin &nbsp;•&nbsp; January 27, 2025</div>
  </div>
  <div class="abs post" style="left:422px">
    <div class="ph" role="img" aria-label="Library shelves with marble busts" style="background:linear-gradient(90deg,#3a3a3a,#9a9a9a 40%,#4a3a2a)"></div>
    <div class="post-title">Why Getting A Consultant Is The Best Decision</div>
    <div class="post-meta">Admin &nbsp;•&nbsp; January 27, 2025</div>
  </div>
  <div class="abs post" style="left:806px">
    <div class="ph" role="img" aria-label="Courthouse interior with columns" style="background:linear-gradient(90deg,#2a2018,#7a5a38 55%,#c9a36a)"></div>
    <div class="post-title">Research And Strategy Are Vital For The Market</div>
    <div class="post-meta">Admin &nbsp;•&nbsp; January 27, 2025</div>
  </div>
</div>

<!-- Footer -->
<footer class="abs footer">
  <svg class="abs" style="left:0;top:0" width="1200" height="510" viewBox="0 0 1200 510"><path d="M0 20 C60 0 120 10 160 60 C240 160 260 300 560 440 L0 440Z" fill="#363251" opacity=".6"/></svg>
  <div class="abs brand"><i></i>HALLORAND</div>
  <p class="abs footer-about">We Focused on Excellence in Trial and Litigation Law Relentless Advocacy, Strategic Solutions Unwavering Commitment to Justice</p>
  <div class="abs social" style="left:61px"></div>
  <div class="abs social" style="left:117px"></div>
  <div class="abs social" style="left:173px"></div>
  <div class="abs social" style="left:229px"></div>

  <div class="abs col-title" style="left:499px">Contact Us</div>
  <div class="abs col-text" style="left:499px;top:166px">Suite 210, 48 Harbor Lane<br>Florida , FL , 3300</div>
  <div class="abs col-text" style="left:499px;top:232px">1800-555-027<br>info@hallorandfirm.com</div>

  <div class="abs col-title" style="left:859px">What We Do</div>
  <div class="abs col-list" style="left:859px;top:162px">TRANSPORTATION LIABILITY<br>REAL ESTATE LAWS<br>PROFESSIONAL LIABILITY<br>WARRANTY CLAIMS<br>COMPLEX BUSINESS DISPUTES</div>

  <div class="abs bottom">
    <span>© 2025 . All rights reserved Hallorand Trial Firm PLLC</span>
    <nav><b>Home</b><span>Practice Areas</span><span>Attorney</span><span>Advisories</span><span>Blog</span></nav>
  </div>
</footer>

</body>
</html>
```